Dynamic Website Design For Dynamic Speaker and Business Coach!

Professional Website Design for a for a Professional Business coach, Business trainer, and Speaker.

Note: This is for design only. No coding required. We want to see your ideas for a great website! This will be a FUN design and not boring like others you may work on.

Please let your creative ideas flow. We have given you a ton of info along with videos to help you understand what we are after, however we WANT your creativity to shine through in your designs!

We are a professional company that has run hundreds of crowdsourced projects on multiple platforms. If you participate in this contest (we hope you do) you can expect great video feedback, consistent feedback, and also our guarantee that if we know your website design will not be what we are looking for we will notify you so you don’t waste your time if there is no chance of you winning.

We respect and recognize this is how you make your living and we will not play games. We look forward to an awesome contest and awesome website designs.

Design Brief:

We are looking for a fresh and fun new design for

http://www.grovepath7.net

This individual (Dana Wilcox) teaches and trains corporations and businesses in the fields of leadership, sales, communication, business operations etc. Additionally this business teaches and mentors business professionals in a small group level or 1 on 1.

The website needs to convey trust, professionalism, and affluent, while at the same time having some personality!

This business operates on 3 core principles that we would like to see incorporated into the logo if it is a good fit. The 3 principals are:

Focus
Accountability
Results

Here is a video to help explain what we like about the current site and what we don’t like:
http://clipvault.example/t/Qm7rTpLw2xKa

As you can see the website is geared towards business professionals. Please look over the website to learn what they do. Obviously this is not a good website so we need your help.

We want a website that is professional-looking, has personality and is geared more towards promoting Dana Wilcox, the owner of Grovepath 7 Partners as a Speaker and Business Consultant. The more you can incorporate clean, professional and fun personality elements into the design, the better off you are at winning.

Here are some examples of other sites in their business that have some things we like:

http://hemlineplays.example Please watch video to learn what we like and don’t like:
http://clipvault.example/t/NrpW3kTyvQa

http://tallpinepromo.example Please watch video to learn what we like and don’t like:
http://clipvault.example/t/K9wPzmRu

http://www.marlaquint.example Please watch video to learn what we like and don’t like:
http://clipvault.example/t/Vx2pq7N5a81

http://www.dwl7z.example Please watch video to learn what we like and don’t like:
http://clipvault.example/t/8K3wuhTzbnx

NOTE: We do not want to copy anything outright. We want to learn, model and take their ideas and make them better. We also want to be flexible and take what we like along with your creativity to make an amazing design.

Here is what we are looking for in more specific terms:

Colors: We like the darker blue (not the light blue like the site) and also a burnt orange. I’ve attached her Logo so you can get an idea and feel for the colors.

When looking at colors please know that the current site and look is NOT what we are going for. We are going for a clean and professional look but also a look that is BOLD, FUN, and Vibrant (hence the colors).

Menu: Horizontal. We like bold and easy to read menu items. Don’t make it small and cluttered.

Site Structure: Clean and easy to navigate. We have a lot of content to display so we need a clean structure that breaks up the text and content areas.
Images: Please pull images from the current site. We can always replace the images of course, but if you show them “their own stuff” in the new design you will be closer to winning because it will feel more like “them”

Look and Feel: Professional. Fun. High-End. Business-like. This website needs to convey that Dana Wilcox and Grovepath 7 Partners are professional. That Dana Wilcox is a sought-after Speaker and Business Consultant who knows what she is talking about; can be serious when she needs to be, but also likes to have fun with her clients. This site must convey that!

Content Areas: It is a safe bet that if it is on the current site we need it on the new site. So don’t drop anything as it makes it hard to “cut content”.

What we don't want: We do not want clutter, boring, or templates or themes. We don’t want too cartoony, too cute, or too fancy… Be creative!

Out of respect to professional designers who really are working hard to win if you do not follow this brief, you submit worn out themes, templates, or boring designs you will be eliminated. We are offering great prize money for this so we expect great visual designs.

Reason: Our client is out of town, and waiting to hear feedback from them. So, in the meantime, we wanted to keep the project going to see what else you designers can come up with. As soon as we hear back from our client, we will pass along the info. Thanks!

Target Market(s)

Target Audience is entrepreneurs and business professionals alike. This is all business to business stuff.

This person teaches and trains startups and billion dollar companies. The common thread is that they are all businesses and companies who need help in various areas including sales, communication, business operations, etc.

Industry/Entity Type

Business

Font styles to use
Sans Serif

Requirements
Must have
• Brief is very detailed. Please review
Nice to have
Should not have

```html
<!DOCTYPE html>
<html lang="en">
<head>
<meta charset="utf-8">
<title>Grovepath 7 Partners – Business Coaching and Consulting</title>
<link href="https://fonts.googleapis.com/css2?family=Ubuntu:wght@300;400;500;700&family=Marcellus&family=Reenie+Beanie&family=Arimo:wght@400;700&display=swap" rel="stylesheet">
<style>
:root{
  --navy:#1c4f7c;
  --navy-dark:#143b5e;
  --blue:#1f5f95;
  --brand-blue:#1f63b8;
  --yellow:#f3c00f;
  --yellow-band:#eeb71a;
  --yellow-mid:#cf9e12;
  --text:#5a5a5a;
  --card:#ebebeb;
  --white:#ffffff;
}
*{box-sizing:border-box;margin:0;padding:0}
html,body{width:850px;height:1200px;overflow:hidden;background:var(--white)}
body{position:relative;font-family:"Ubuntu",sans-serif;color:var(--text)}
.abs{position:absolute}

/* header */
.brand{left:18px;top:22px;display:flex;align-items:center;gap:10px}
.brand-dot{width:44px;height:44px;border-radius:50%;background:var(--brand-blue)}
.brand-name{font-weight:700;font-size:25px;color:var(--brand-blue);line-height:1}
.phone-top{left:500px;top:18px;display:flex;align-items:center;gap:8px;font-family:"Arimo",sans-serif;font-weight:700;font-size:22px;color:var(--navy)}
.search{left:527px;top:56px;width:166px;height:21px;border:1px solid #b5b5b5;font-family:"Arimo",sans-serif;font-size:10px;color:#777;padding:4px 6px}
.search svg{position:absolute;right:5px;top:4px}
.sharing{left:724px;top:16px;font-family:"Reenie Beanie",cursive;font-size:15px;color:#555}
.social-top{left:727px;top:45px;display:flex;gap:9px}
.social-top span,.social-foot span{display:block;width:29px;height:29px;border-radius:4px;background:#2d5c9e}
.social-top span:nth-child(2),.social-foot span:nth-child(2){background:#3f93c8}
.social-top span:nth-child(3),.social-foot span:nth-child(3){background:#1d6aa2}

/* nav */
.nav{left:0;top:96px;width:850px;height:33px;background:linear-gradient(#21588a,var(--navy-dark));display:flex}
.nav a{display:block;height:33px;line-height:33px;padding:0 13.3px;color:var(--white);font-weight:500;font-size:12px;text-decoration:none;border-right:1px solid #2f6899}
.nav a.active{background:var(--navy-dark)}

/* hero */
.hero{left:0;top:129px;width:850px;height:265px;background:linear-gradient(#dcdcdc,#f4f4f4 40%,#eeeeee)}
.video{left:40px;top:155px;width:386px;height:217px;background:linear-gradient(110deg,#2e78b3,#1c5a92 60%,#16476f);overflow:hidden}
.video-person{position:absolute;right:40px;top:6px;width:110px;height:211px;background:linear-gradient(#6a4a3a,#3a3a3f 45%,#2a2a2e)}
.video-title{position:absolute;left:10px;top:22px;width:250px;text-align:center;font-family:"Marcellus",serif;color:var(--white);font-size:35px;line-height:37px}
.video-title .sm{font-size:31px}
.video-send{position:absolute;right:8px;top:7px;width:21px;height:21px;background:rgba(0,0,0,.55);border-radius:2px}
.video-bar{position:absolute;left:6px;bottom:6px;width:374px;height:22px}
.play{position:absolute;left:0;top:0;width:39px;height:22px;background:rgba(0,0,0,.75);border-radius:2px}
.track{position:absolute;left:42px;top:2px;width:332px;height:18px;background:rgba(0,0,0,.6)}
.track i{position:absolute;left:8px;top:8px;width:272px;height:3px;background:#333;border:1px solid #777}
.time{position:absolute;left:46px;top:-7px;background:#fff;color:#222;font-size:6px;padding:0 2px;font-family:"Arimo",sans-serif}
.hd{position:absolute;right:6px;top:5px;font:700 8px "Arimo",sans-serif;color:#999;font-style:italic}
.hero-copy{left:470px;top:182px;width:340px;text-align:center}
.hero-copy h1{font-family:"Arimo",sans-serif;font-weight:400;font-size:26.5px;line-height:29px;color:var(--blue)}
.hero-copy .ask{margin:12px auto 0;width:246px;border-top:1px solid #777;border-bottom:1px solid #777;padding:3px 0 4px;font-size:17px;color:#555;letter-spacing:.2px}
.btn-hero{left:563px;top:302px;width:152px;height:40px;background:linear-gradient(var(--yellow),#e9b00a);border-radius:2px;font-family:"Arimo",sans-serif;font-weight:700;font-size:15px;color:#6b4700;text-align:center;line-height:40px}

/* left column */
.portrait{left:40px;top:426px;width:178px;height:267px;background:linear-gradient(#5c5c5c,#7a6a5c 55%,#8aa6b4);overflow:hidden}
.portrait .cap{position:absolute;left:0;bottom:0;width:100%;height:51px;background:rgba(240,180,20,.88);color:var(--white);font-weight:500;font-size:17px;line-height:51px;text-align:center;letter-spacing:.3px}
.testimonial{left:40px;top:706px;width:179px;height:277px;border:1px solid #9b9b9b;padding:10px 9px}
.testimonial h3{font-weight:500;font-size:16px;color:var(--blue);padding-bottom:7px;border-bottom:1px solid #aaa;display:flex;align-items:center;gap:7px}
.testimonial h3 b{color:var(--yellow);font-family:"Marcellus",serif;font-size:26px;line-height:14px;height:14px}
.testimonial p{margin-top:11px;font-weight:300;font-size:11px;line-height:17px;color:#555}
.testimonial .who{margin-top:5px;font-weight:400;font-size:11.5px;line-height:13.5px;color:#333}
.badges{left:57px;top:1000px;display:flex;gap:15px}
.badges span{display:block;width:42px;height:42px;border-radius:50%;background:#2d5f8f;border:3px solid #b9a15a}
.badges span:nth-child(2){background:#2a4f86;border-color:#c9a43a}
.badges span:nth-child(3){border-radius:0;background:linear-gradient(#f4f0ea 45%,#b3452d);border:1px solid #999;width:40px}

/* main copy */
.intro{left:246px;top:432px;width:545px;font-weight:300;font-size:11.8px;line-height:19.2px;color:#555}
.cards{left:244px;top:528px;display:flex;gap:13px}
.card{width:179px;height:345px;background:var(--card);text-align:center;position:relative}
.card .ic{margin:20px auto 0;width:80px;height:80px;border-radius:50%;background:var(--yellow);border:4px solid var(--white);box-shadow:0 0 0 1px #e0e0e0;display:flex;align-items:center;justify-content:center}
.card h2{margin:16px auto 0;width:160px;font-weight:500;font-size:14.5px;line-height:17px;color:var(--blue)}
.card p{margin:16px auto 0;width:158px;font-weight:300;font-size:10.5px;line-height:16.8px;color:#606060}
.card .more{position:absolute;left:36px;top:303px;width:106px;height:26px;background:linear-gradient(var(--yellow),#e9ae08);border-radius:2px;font-family:"Arimo",sans-serif;font-weight:700;font-size:11px;line-height:26px;color:#4e3300}
.outro{left:246px;top:897px;width:580px;font-weight:300;font-size:11.8px;line-height:19.2px;color:#555}

/* footer */
.foot{left:0;top:1100px;width:850px;height:100px;background:linear-gradient(#1d5f93,#195684)}
.contact-bar{left:38px;top:1062px;width:768px;height:66px;background:var(--yellow-band);display:flex}
.contact-bar .cell{display:flex;align-items:center;gap:9px;color:var(--white);font-size:19px;font-weight:400}
.cell.phone{width:227px;padding-left:14px}
.cell.mail{width:281px;background:var(--yellow-mid);padding-left:20px;font-size:17px}
.social-foot{display:flex;gap:8px;padding-left:34px;align-items:center}
.foot-links{left:0;top:1146px;width:850px;text-align:center;color:var(--white);font-weight:500;font-size:11px}
.copy{left:0;top:1165px;width:850px;text-align:center;color:#e3ecf4;font-weight:300;font-size:10.5px}
</style>
</head>
<body>

<header>
  <div class="abs brand"><span class="brand-dot"></span><span class="brand-name">Grovepath 7 Partners</span></div>
  <div class="abs phone-top">
    <svg width="16" height="18" viewBox="0 0 16 18"><path d="M3 1l3 4-2 2c1 3 3 5 6 6l2-2 4 3-2 3C7 17 0 9 1 3z" fill="#1c1c1c"/></svg>
    (505)418-2793
  </div>
  <div class="abs search">Search
    <svg width="12" height="12" viewBox="0 0 12 12"><circle cx="5" cy="5" r="3.7" fill="none" stroke="#333" stroke-width="1.4"/><path d="M7.7 7.7L11 11" stroke="#333" stroke-width="1.6"/></svg>
  </div>
  <div class="abs sharing">Sharing is caring!</div>
  <div class="abs social-top" aria-label="Social links"><span></span><span></span><span></span></div>
</header>

<nav class="abs nav">
  <a class="active">Home</a><a>Passion</a><a>Who We Are</a><a>Speaker</a><a>Free Videos</a><a>Web TV Show</a><a>Testimonials</a><a>Brightway Learning</a><a>Blog</a><a style="border-right:0">Contact</a>
</nav>

<section class="abs hero"></section>
<div class="abs video">
  <div class="video-person" role="img" aria-label="Video still of the coach speaking on a blue studio backdrop"></div>
  <div class="video-title">Do You Need<br>More Focus,<br><span class="sm">Accountability</span><br><span class="sm">&amp; Results?</span></div>
  <div class="video-send"><svg width="21" height="21" viewBox="0 0 21 21"><path d="M5 11l11-6-4 12-2-4z" fill="#fff"/></svg></div>
  <div class="video-bar">
    <div class="play"><svg width="39" height="22" viewBox="0 0 39 22"><path d="M15 6l10 5-10 5z" fill="#fff"/></svg></div>
    <div class="track"><span class="time">01:46</span><i></i><span class="hd">HD</span></div>
  </div>
</div>
<div class="abs hero-copy">
  <h1>Albuquerque Business<br>Coaching and Consulting</h1>
  <div class="ask">What do you want more of?</div>
</div>
<div class="abs btn-hero">FIND OUT MORE</div>

<aside>
  <div class="abs portrait" role="img" aria-label="Portrait photo of Dana Wilcox">
    <div class="cap">DANA WILCOX</div>
  </div>
  <div class="abs testimonial">
    <h3><b>“</b>Testimonial</h3>
    <p>“Dana is an enthusiastic and engaging instructor who strives at every opportunity to provide a worthwhile and purposeful workshop to her audience. She is fun, easy to work with, and full of great information! A real asset to any organization looking for professional training.”</p>
    <div class="who">Morgan Ellery -<br>Former Advanced Sales<br>Training Manager</div>
  </div>
  <div class="abs badges" aria-label="Membership badges"><span></span><span></span><span></span></div>
</aside>

<main>
  <p class="abs intro">Are you searching to bridge the gap between where you are and where you want to be? As you face greater pressure to “move the needle” on your company’s productivity and bottom line profitability, how prepared are you to step in and shine as the leader? We specialize in guiding leaders to become easier to follow.  You’re in the Right Place.</p>

  <div class="abs cards">
    <article class="card">
      <div class="ic"><svg width="40" height="44" viewBox="0 0 40 44"><circle cx="20" cy="12" r="9" fill="#fff"/><path d="M3 43c0-14 7-20 17-20s17 6 17 20z" fill="#fff"/><path d="M18 24h4l-1 10h-2z" fill="#f3c00f"/></svg></div>
      <h2>Albuquerque Business Coach: Focus, Accountability, &amp; Results</h2>
      <p>Whether you’re leading a company, or are an employee, all of us have a role to play in contributing to the profit and the future of the company.</p>
      <div class="more">Read More</div>
    </article>
    <article class="card">
      <div class="ic"><svg width="46" height="42" viewBox="0 0 46 42"><rect x="4" y="28" width="7" height="13" fill="#fff"/><rect x="14" y="22" width="7" height="19" fill="#fff"/><rect x="24" y="17" width="7" height="24" fill="#fff"/><rect x="34" y="11" width="7" height="30" fill="#fff"/><path d="M3 22L17 10l8 6L40 3" stroke="#fff" stroke-width="3" fill="none"/><path d="M34 2h8v8z" fill="#fff"/></svg></div>
      <h2>Your organization expects you to deliver value by delivering results</h2>
      <p>At Grovepath 7 Partners, we know as a company or as individuals, clarity of the direction captured in an annual plan that is monitored monthly is one of the surest…</p>
      <div class="more">Read More</div>
    </article>
    <article class="card">
      <div class="ic"><svg width="50" height="36" viewBox="0 0 50 36"><path d="M1 8l9-4 6 14-8 4z" fill="#fff"/><path d="M49 8l-9-4-6 14 8 4z" fill="#fff"/><path d="M13 8l9-3 6 3 8-2 5 12-10 12c-2 2-4 2-6 0l-10-9z" fill="#fff"/><path d="M20 14l6-3 8 8" stroke="#f3c00f" stroke-width="2" fill="none"/></svg></div>
      <h2>Grovepath 7 Partners has delivered on our promise</h2>
      <p>With over 25 years of experience in a variety of industries, we know the daily attitudes, habits and goals for successful companies begin with a plan.</p>
      <div class="more">Read More</div>
    </article>
  </div>

  <p class="abs outro">With over 25 years of experience in a variety of industries, we know the daily attitudes, habits and goals for successful companies begin with a plan.  By training employees where needed and coaching to clear expectations writes success stories daily as the plan unfolds over the course of the year.</p>
</main>

<footer>
  <div class="abs foot"></div>
  <div class="abs contact-bar">
    <div class="cell phone">
      <svg width="22" height="18" viewBox="0 0 22 18"><path d="M1 6c0-4 20-4 20 0v2h-5V5H6v3H1z" fill="#fff"/><path d="M5 9h12l3 8H2z" fill="#fff"/><circle cx="11" cy="13" r="2.2" fill="#eeb71a"/></svg>
      (505)418-2793
    </div>
    <div class="cell mail">
      <svg width="24" height="18" viewBox="0 0 24 18"><rect x="1" y="1" width="22" height="16" fill="#fff"/><path d="M1 1l11 9 11-9" stroke="#cf9e12" stroke-width="2" fill="none"/></svg>
      dana@grovepath7.net
    </div>
    <div class="social-foot" aria-label="Social links"><span></span><span></span><span></span></div>
  </div>
  <div class="abs foot-links">Passion | Who We Are | Speaker | Free Videos | Web TV Show | Testimonials | Brightway Learning | Blog | Contact</div>
  <div class="abs copy">©2014 Grovepath 7 Partners</div>
</footer>

</body>
</html>
```